Real Estate Development, Finance and Fund Management company

We need a business card and logo design for a new company based in Asia called 'Vantor Holdings Ltd.'
We provide full service large scale real estate development services, including fund management, project delivery services and acquisitions. We are looking for a bold logo with a strong feeling of security. A good reference would be the Marlowgate (www.marlowgate-example.com) or Tesmere Equity (www.tesmereeq-example.com).
We will need to have the imagery for the cards and logos to be produced for a dark and light background, and for web and print quality.
Initial thoughts are to have silver text on a black or dark grey background but leave that to your discretion.
Final design should communicate stability, financial safety and building on a solid foundation.
NOTE : We are not looking for pictures or clip art. Logo should be primarily from text and anything additional should be limited and tasteful.
Thanks!

```html
<!DOCTYPE html>
<html lang="en">
<head>
<meta charset="utf-8">
<title>Vantor Holdings Ltd. – Business Card</title>
<link rel="stylesheet" href="https://fonts.googleapis.com/css2?family=Raleway:wght@300&family=Arimo:wght@400;700&family=Tinos:wght@700&display=swap">
<style>
  :root {
    --page: #ffffff;
    --panel-dark-top: #1b1d21;
    --panel-dark-bottom: #0a0b0d;
    --panel-steel-top: #3d444c;
    --panel-steel-bottom: #272c33;
    --back-light: #4a535c;
    --back-dark: #15181c;
    --divider: #5a6069;
    --silver: #c9ccd0;
    --name-grey: #5d6166;
    --text-light: #f2f3f5;
    --icon: #d9dce0;
  }
  * { box-sizing: border-box; margin: 0; padding: 0; }
  html, body {
    width: 1026px; height: 1200px; overflow: hidden;
    background: var(--page);
  }
  .canvas { position: relative; width: 1026px; height: 1200px; }
  .card {
    position: absolute; left: 50px; width: 926px; height: 505px;
    border-radius: 22px; overflow: hidden;
  }
  .card--front {
    top: 48px;
    background: linear-gradient(180deg, var(--panel-steel-top), var(--panel-steel-bottom));
  }
  .card--back {
    top: 640px;
    background: radial-gradient(ellipse at 20% 10%, var(--back-light) 0%, #2b3138 55%, var(--back-dark) 100%);
  }
  .identity-panel {
    position: absolute; left: 0; top: 0; width: 392px; height: 100%;
    background: linear-gradient(180deg, var(--panel-dark-top), var(--panel-dark-bottom));
    border-right: 2px solid var(--divider);
    text-align: center;
  }
  .person-name {
    position: absolute; left: 0; right: 0; top: 203px;
    font-family: "Tinos", serif; font-weight: 700; font-size: 44px;
    color: var(--name-grey);
  }
  .person-role {
    position: absolute; left: 0; right: 0; top: 266px;
    font-family: "Arimo", sans-serif; font-weight: 700; font-size: 32px;
    color: var(--text-light);
  }
  .brand-name {
    font-family: "Raleway", sans-serif; font-weight: 300;
    color: var(--silver); white-space: nowrap; letter-spacing: -0.5px;
  }
  .card--front .brand-name {
    position: absolute; left: 414px; top: 28px; font-size: 47px;
  }
  .contact-list {
    position: absolute; right: 48px; top: 176px; list-style: none;
    font-family: "Arimo", sans-serif; font-size: 29px; color: var(--text-light);
  }
  .contact-item {
    display: flex; justify-content: flex-end; align-items: center;
    gap: 26px; margin-bottom: 14px; line-height: 34px;
  }
  .contact-item--address { line-height: 35px; }
  .contact-item--email { margin-top: -6px; }
  .contact-text { text-align: right; }
  .contact-icon { width: 30px; height: 30px; flex: none; }
  .back-lockup {
    position: absolute; left: 0; right: 0; top: 170px;
    width: 540px; margin: 0 auto; text-align: right;
  }
  .card--back .brand-name { font-size: 54px; text-align: center; }
  .web-address {
    font-family: "Arimo", sans-serif; font-size: 29px; color: var(--text-light);
    margin-top: 2px;
  }
</style>
</head>
<body>
<main class="canvas">
  <section class="card card--front">
    <div class="identity-panel">
      <p class="person-name">Aldric Fenn</p>
      <p class="person-role">Director</p>
    </div>
    <p class="brand-name">Vantor Holdings Ltd.</p>
    <ul class="contact-list">
      <li class="contact-item contact-item--address">
        <span class="contact-text">2270 Harbor Ridge Rd,<br>Kelmont South Carolina</span>
        <svg class="contact-icon" viewBox="0 0 30 30" aria-hidden="true"><path d="M4 15 L15 5 L26 15 H23 V25 H17 V18 H13 V25 H7 V15 Z" fill="var(--icon)"/></svg>
      </li>
      <li class="contact-item">
        <span class="contact-text">03 4920 6618</span>
        <svg class="contact-icon" viewBox="0 0 30 30" aria-hidden="true"><path d="M3 12 Q15 4 27 12 L25 15 L20 13 L20 11 Q15 9 10 11 L10 13 L5 15 Z" fill="var(--icon)"/><path d="M8 16 H22 L25 24 H5 Z" fill="var(--icon)"/></svg>
      </li>
      <li class="contact-item">
        <span class="contact-text">03 4920 6618</span>
        <svg class="contact-icon" viewBox="0 0 30 30" aria-hidden="true"><rect x="9" y="4" width="12" height="9" fill="none" stroke="var(--icon)" stroke-width="2"/><rect x="5" y="13" width="20" height="10" rx="2" fill="var(--icon)"/><rect x="8" y="23" width="14" height="3" fill="var(--icon)"/></svg>
      </li>
      <li class="contact-item">
        <span class="contact-text">0427 318 904</span>
        <svg class="contact-icon" viewBox="0 0 30 30" aria-hidden="true"><rect x="9" y="3" width="12" height="24" rx="2" fill="none" stroke="var(--icon)" stroke-width="2"/><rect x="11" y="6" width="8" height="15" fill="var(--icon)"/></svg>
      </li>
      <li class="contact-item contact-item--email">
        <span class="contact-text">vantor@example.com</span>
        <svg class="contact-icon" viewBox="0 0 30 30" aria-hidden="true"><rect x="3" y="8" width="24" height="15" fill="var(--icon)"/><path d="M3 8 L15 17 L27 8" fill="none" stroke="#2b3036" stroke-width="1.6"/></svg>
      </li>
    </ul>
  </section>

  <section class="card card--back">
    <div class="back-lockup">
      <p class="brand-name">Vantor Holdings Ltd.</p>
      <p class="web-address">www.vantor-example.com</p>
    </div>
  </section>
</main>
</body>
</html>
```